A start up special flyer design!

Hi All - Have updated the attachment content - This is the info required for the designs.
I need a catchy flyer to send out to a few areas to advertise the start of my plumbing business!
The flyer will contain an offer for customers, which will need to have some key details on it. See attached. Feel free to fit these criteria into the flyer given your knowledge on design and messaging principles. Key thing to get across to customers is the discount and special offer, and that it is a start up offer.
I have a logo that needs to be on the flyer as well - let me know what format you require and I will send through to you.
The color scheme needs to be blue / grey / black / white.
Let me know if you have any questions.
I

```html
<!DOCTYPE html>
<html lang="en">
<head>
<meta charset="utf-8">
<title>Harbour Line Plumbing – Start-up Offer Flyer &amp; Cards</title>
<link href="https://fonts.googleapis.com/css2?family=Roboto+Condensed:ital,wght@0,400;0,700;1,400;1,700&family=Roboto:wght@400;500;700&display=swap" rel="stylesheet">
<style>
  :root{
    --bg:#e6e8eb;
    --blue:#0e4f8f;
    --blue-mid:#1a78bd;
    --blue-light:#4aa8d8;
    --blue-pale:#7cc3e6;
    --navy:#1f3a6e;
    --orange:#e0661c;
    --grey:#7b7f84;
    --ink:#1c1c1c;
    --white:#ffffff;
  }
  *{margin:0;padding:0;box-sizing:border-box}
  html,body{width:1200px;height:1000px;overflow:hidden;background:var(--bg)}
  body{position:relative;font-family:"Roboto",Arial,sans-serif;color:var(--ink)}
  .abs{position:absolute}
  .cond{font-family:"Roboto Condensed","Arial Narrow",sans-serif}

  /* Flyer */
  .flyer{position:absolute;left:42px;top:72px;width:664px;height:858px;background:var(--white);overflow:hidden;box-shadow:0 4px 14px rgba(0,0,0,.25)}
  .flyer svg.shapes{position:absolute;left:0;top:0}
  .photo-worker{left:236px;top:640px;width:238px;height:218px;border-radius:60px 60px 0 0;background:linear-gradient(180deg,#34558c,var(--navy))}
  .offer-big{left:414px;top:94px;color:var(--white);font-weight:700;font-size:76px;line-height:1;letter-spacing:-1px}
  .offer-off{left:572px;top:104px;color:var(--white);font-weight:700;font-size:24px;writing-mode:vertical-rl;letter-spacing:1px}
  .offer-sub{left:420px;top:172px;color:var(--white);font-weight:700;font-size:18px}
  .bonus{left:413px;top:216px;width:240px;color:var(--white);font-size:21px;line-height:25px;text-transform:uppercase}
  .services-title{left:375px;top:378px;color:var(--white);font-weight:700;font-size:31px}
  .service-list{left:382px;top:444px;width:250px;list-style:none;color:var(--white);font-size:20px;line-height:25px}
  .service-list li{position:relative;padding-left:26px;margin-bottom:25px}
  .service-list svg{position:absolute;left:0;top:2px}
  .brand{left:20px;top:445px;width:300px;text-align:center;color:var(--blue);font-weight:700;font-size:30px;line-height:34px;letter-spacing:1px}
  .brand .dot{display:inline-block;width:14px;height:14px;border-radius:50%;background:var(--blue);margin-bottom:6px}
  .appointment{left:25px;top:640px;width:210px;font-size:15px;line-height:20px;color:#333}
  .appointment strong{color:var(--blue-mid);font-size:17px}
  .appointment em{font-style:normal;color:var(--blue-mid)}
  .phone{left:25px;top:758px;font-size:26px;font-weight:700;color:var(--ink);display:flex;align-items:center;gap:6px}
  .contact-line{left:28px;font-size:12px;color:#333;display:flex;align-items:center;gap:8px}
  .footnote{left:490px;top:780px;width:170px;color:var(--white);font-style:italic;font-size:10.5px;line-height:13px}

  /* Cards */
  .card{position:absolute;left:740px;width:393px;height:236px;overflow:hidden;box-shadow:0 3px 10px rgba(0,0,0,.25)}
  .card-front{top:242px;background:var(--blue)}
  .card-front .brand-card{position:absolute;left:0;top:90px;width:100%;text-align:center;color:var(--white);font-weight:700;font-size:28px;letter-spacing:1px}
  .card-back{top:534px;background:var(--white)}
  .card-back .photo-card{position:absolute;left:230px;top:70px;width:142px;height:142px;border-radius:40px 40px 0 0;background:linear-gradient(180deg,#34558c,var(--navy))}
  .card-back .brand-card{position:absolute;left:22px;top:52px;color:var(--blue);font-weight:700;font-size:19px;line-height:22px;letter-spacing:1px}
  .card-back .tagline{position:absolute;left:30px;top:102px;font-size:8.5px;color:#333;letter-spacing:.3px}
  .card-back .info{position:absolute;left:24px;font-size:10px;color:#333;display:flex;align-items:center;gap:6px}
  .card-back .web{position:absolute;left:202px;top:218px;font-size:10px;color:var(--white);display:flex;align-items:center;gap:6px}
</style>
</head>
<body>

<section class="flyer" aria-label="Start-up offer flyer">
  <svg class="shapes" width="664" height="858" viewBox="0 0 664 858">
    <defs>
      <linearGradient id="panel" x1="0" y1="0" x2="1" y2="1">
        <stop offset="0" stop-color="#5fb6e2"/>
        <stop offset="1" stop-color="#2c8cc9"/>
      </linearGradient>
      <linearGradient id="photoTop" x1="0" y1="0" x2="1" y2="1">
        <stop offset="0" stop-color="#c9d3dc"/>
        <stop offset=".5" stop-color="#3f6fa6"/>
        <stop offset="1" stop-color="#d8dde2"/>
      </linearGradient>
    </defs>
    <polygon points="420,0 664,0 664,858 330,858 398,383" fill="url(#panel)"/>
    <polygon points="0,0 432,0 402,386 0,346" fill="url(#photoTop)" role="img" aria-label="Photo of a plumber repairing pipes under a sink"/>
    <polygon points="0,346 402,386 398,392 0,354" fill="var(--blue-mid)"/>
    <polygon points="380,92 598,88 592,176 376,196" fill="var(--orange)"/>
    <polygon points="355,372 628,372 636,424 352,424" fill="var(--blue)"/>
    <rect x="0" y="842" width="664" height="16" fill="var(--blue-pale)"/>
  </svg>

  <div class="abs photo-worker" role="img" aria-label="Photo of a smiling plumber in navy overalls holding a pipe wrench"></div>

  <div class="abs offer-big cond">15%</div>
  <div class="abs offer-off cond">OFF</div>
  <div class="abs offer-sub cond">YOUR OVERALL BILL*</div>
  <p class="abs bonus cond">Plus, a free hot water heater health check and replacement quote**</p>

  <h2 class="abs services-title cond">Services Offered</h2>
  <ul class="abs service-list cond">
    <li><svg width="20" height="20" viewBox="0 0 20 20"><path d="M2 11 L8 17 L19 3" fill="none" stroke="var(--blue)" stroke-width="3.5" stroke-linecap="round"/></svg>All Plumbing, Draining, And Gasfitting Works</li>
    <li><svg width="20" height="20" viewBox="0 0 20 20"><path d="M2 11 L8 17 L19 3" fill="none" stroke="var(--blue)" stroke-width="3.5" stroke-linecap="round"/></svg>Quality Work At A Decent Price</li>
    <li><svg width="20" height="20" viewBox="0 0 20 20"><path d="M2 11 L8 17 L19 3" fill="none" stroke="var(--blue)" stroke-width="3.5" stroke-linecap="round"/></svg>Local Plumber</li>
  </ul>

  <div class="abs brand"><span class="dot"></span><br>HARBOUR LINE<br>PLUMBING</div>

  <p class="abs appointment">To make an appointment,<br><strong>call or email Sam,</strong><br>or alternatively make a<br><em>booking directly on the website</em></p>

  <div class="abs phone">
    <svg width="24" height="24" viewBox="0 0 24 24"><circle cx="12" cy="12" r="10.5" fill="none" stroke="var(--blue-mid)" stroke-width="2"/><path d="M8 6.5 L10 6.5 L11 9.5 L9.7 10.6 Q11 13.5 13.4 14.3 L14.5 13 L17.5 14 L17.5 16 Q12 18 7 10 Z" fill="var(--blue-mid)"/></svg>
    0400 555 218
  </div>
  <div class="abs contact-line" style="top:796px">
    <svg width="14" height="10" viewBox="0 0 14 10"><rect x=".5" y=".5" width="13" height="9" fill="none" stroke="var(--blue-mid)"/><path d="M.5 .5 L7 6 L13.5 .5" fill="none" stroke="var(--blue-mid)"/></svg>
    sam@harbourlineplumbing.com
  </div>
  <div class="abs contact-line" style="top:814px">
    <svg width="14" height="14" viewBox="0 0 14 14"><circle cx="7" cy="7" r="6" fill="none" stroke="var(--blue-mid)"/><path d="M1 7 H13 M7 1 V13" stroke="var(--blue-mid)"/></svg>
    www.harbourlineplumbing.com
  </div>

  <p class="abs footnote cond">*Offer expires <b>31 October 2016</b><br>**Quote valid for <b>12 months</b> from the quote date.</p>
</section>

<section class="card card-front" aria-label="Business card front">
  <div class="brand-card">HARBOUR LINE<br><span style="font-size:20px;letter-spacing:6px">PLUMBING</span></div>
</section>

<section class="card card-back" aria-label="Business card back">
  <div class="photo-card" role="img" aria-label="Photo of a smiling plumber with arms crossed holding a wrench"></div>
  <div class="brand-card">HARBOUR LINE<br><span style="letter-spacing:5px">PLUMBING</span></div>
  <div class="tagline">PLUMBING • DRAINING • GASFITTING WORKS</div>
  <div class="info" style="top:168px">
    <svg width="11" height="11" viewBox="0 0 24 24"><circle cx="12" cy="12" r="10.5" fill="none" stroke="var(--blue)" stroke-width="2"/><path d="M8 6.5 L10 6.5 L11 9.5 L9.7 10.6 Q11 13.5 13.4 14.3 L14.5 13 L17.5 14 L17.5 16 Q12 18 7 10 Z" fill="var(--blue)"/></svg>
    0400 555 218
  </div>
  <div class="info" style="top:188px">
    <svg width="12" height="9" viewBox="0 0 14 10"><rect x=".5" y=".5" width="13" height="9" fill="none" stroke="var(--blue)"/><path d="M.5 .5 L7 6 L13.5 .5" fill="none" stroke="var(--blue)"/></svg>
    sam@harbourlineplumbing.com
  </div>
  <svg class="abs" style="left:0;top:212px" width="393" height="24" viewBox="0 0 393 24" aria-hidden="true">
    <rect width="393" height="24" fill="var(--blue)"/>
    <polygon points="180,0 393,0 393,24 172,24" fill="var(--grey)"/>
  </svg>
  <div class="web">
    <svg width="11" height="11" viewBox="0 0 14 14"><circle cx="7" cy="7" r="6" fill="none" stroke="#fff"/><path d="M1 7 H13 M7 1 V13" stroke="#fff"/></svg>
    www.harbourlineplumbing.com
  </div>
</section>

</body>
</html>
```